New business card for civil engineering company - "Keystone Audit"

We need a business card designed for our new structural engineering company.

The company name is "Keystone Audit" logo files attached.

We would like the following:
* Two-sided card
* Simple design

Information to be placed on the card:
Name - Marcus Dellow
Job Title - Director / Structural Engineer
Credentials - BEng(Hons), CPEng, CMengNZ, IntPE(NZ)
Email - marcus.dellow@keystoneaudit.co.nz
mobile - 0219364058
website - www.keystoneaudit.co.nz

```html
<!DOCTYPE html>
<html lang="en">
<head>
<meta charset="utf-8">
<title>Keystone Audit – Business Card</title>
<link rel="stylesheet" href="https://fonts.googleapis.com/css2?family=Rubik:wght@400;500&display=swap">
<style>
  :root {
    --canvas: #e9e6e1;
    --card: #ffffff;
    --ink: #3a3a3c;
    --ink-soft: #6e6e72;
    --rule: #55565a;
    --brand-blue: #4a90d6;
    --band: #4a4a4c;
    --band-text: #ffffff;
    --facet-light: #fafafa;
    --facet-mid: #dcdcdc;
  }
  html, body {
    margin: 0;
    padding: 0;
    width: 900px;
    height: 1200px;
    overflow: hidden;
    background: var(--canvas);
    font-family: "Rubik", Arial, sans-serif;
  }
  .canvas {
    position: relative;
    width: 900px;
    height: 1200px;
  }
  .card {
    position: absolute;
    left: 88px;
    width: 730px;
    box-shadow: 0 6px 18px rgba(0,0,0,0.18);
    overflow: hidden;
  }
  .card--front {
    top: 150px;
    height: 425px;
    background: var(--card);
  }
  .card--back {
    top: 628px;
    height: 427px;
  }

  /* Front */
  .brand-lockup {
    position: absolute;
    display: flex;
    align-items: center;
    gap: 10px;
  }
  .card--front .brand-lockup {
    left: 52px;
    top: 250px;
  }
  .brand-mark {
    width: 18px;
    height: 18px;
    background: var(--brand-blue);
  }
  .brand-name {
    font-weight: 500;
    font-size: 20px;
    letter-spacing: 1px;
    color: var(--ink);
    text-transform: uppercase;
  }
  .divider {
    position: absolute;
    left: 276px;
    top: 128px;
    width: 2px;
    height: 166px;
    background: var(--rule);
  }
  .contact {
    position: absolute;
    left: 307px;
    top: 122px;
    color: var(--ink);
  }
  .contact__name {
    margin: 0;
    font-size: 22px;
    font-weight: 400;
    letter-spacing: 1.5px;
    text-transform: uppercase;
  }
  .contact__name strong { font-weight: 500; }
  .contact__role,
  .contact__credentials {
    margin: 6px 0 0;
    font-size: 15.5px;
    letter-spacing: 1px;
    color: var(--ink-soft);
  }
  .contact__details {
    list-style: none;
    margin: 28px 0 0;
    padding: 0;
    font-size: 15.5px;
    letter-spacing: 1px;
    line-height: 25px;
  }

  /* Back */
  .facet-field {
    position: absolute;
    inset: 0;
    background: radial-gradient(ellipse at 50% 45%, var(--facet-light) 0%, #eeeeee 45%, var(--facet-mid) 100%);
  }
  .card--back .brand-lockup {
    left: 0;
    right: 0;
    top: 270px;
    justify-content: center;
  }
  .card--back .brand-mark { background: var(--band); width: 22px; height: 22px; }
  .card--back .brand-name { font-size: 28px; }
  .web-band {
    position: absolute;
    left: 0;
    right: 0;
    top: 385px;
    height: 20px;
    background: var(--band);
    color: var(--band-text);
    text-align: center;
    font-size: 13px;
    line-height: 20px;
    letter-spacing: 6.5px;
    text-transform: uppercase;
  }
</style>
</head>
<body>
<main class="canvas">
  <section class="card card--front" aria-label="Card front">
    <div class="brand-lockup">
      <span class="brand-mark"></span>
      <span class="brand-name">Keystone Audit</span>
    </div>
    <div class="divider"></div>
    <div class="contact">
      <h1 class="contact__name"><strong>Marcus</strong> Dellow</h1>
      <p class="contact__role">Director / Structural Engineer</p>
      <p class="contact__credentials">BEng(Hons), CPEng, CMengNZ, IntPE(NZ)</p>
      <ul class="contact__details">
        <li>P: 0219364058</li>
        <li>E: marcus.dellow@keystoneaudit.co.nz</li>
        <li>W: www.keystoneaudit.co.nz</li>
      </ul>
    </div>
  </section>

  <section class="card card--back" aria-label="Card back">
    <div class="facet-field" role="img" aria-label="Soft grey low-poly faceted background"></div>
    <div class="brand-lockup">
      <span class="brand-mark"></span>
      <span class="brand-name">Keystone Audit</span>
    </div>
    <div class="web-band">www.keystoneaudit.co.nz</div>
  </section>
</main>
</body>
</html>
```